Novarra clean Business Cards

I'm looking for someone to design my business card using my company name and logo. I would like it it be clean, fresh and a little out of the box. The colors I would like used are the same two in my logo (gold and the teal blue color) I also want it to screen high end scene the company name is Novarra clean :) I'm a commercial cleaning company based out of Orange and San Diego county. Once I receive your email I will send over the file. Because the file is quote big with several options of logos. Please be an out of the box thinker and take some risk...I'm looking for someone to put themselves out there. Thanks and good luck

```html
<!DOCTYPE html>
<html lang="en">
<head>
<meta charset="utf-8">
<title>Novarra clean Business Cards</title>
<link href="https://fonts.googleapis.com/css2?family=Arimo:ital,wght@0,400;1,400&display=swap" rel="stylesheet">
<style>
  :root {
    --teal: #0f6b70;
    --gold: #cc9a06;
    --white: #ffffff;
    --edge: #bdbdbd;
  }
  * { margin: 0; padding: 0; box-sizing: border-box; }
  html, body { width: 1200px; height: 741px; overflow: hidden; background: var(--white); }
  body { position: relative; font-family: "Arimo", Arial, sans-serif; color: var(--teal); }

  .card { position: absolute; width: 590px; height: 360px; overflow: hidden; }
  .card--front { background: var(--white); border: 1px solid var(--edge); }
  .card--back { background: var(--teal); }
  .card-a { left: 1px; top: 1px; }
  .card-b { left: 610px; top: 0; }
  .card-c { left: 1px; top: 379px; }
  .card-d { left: 610px; top: 379px; }

  .corner { position: absolute; inset: 0; width: 100%; height: 100%; }

  .brand { position: absolute; white-space: nowrap; font-weight: 400; line-height: 1; }
  .brand--teal { color: var(--teal); }
  .brand--white { color: var(--white); }
  .brand-a { left: 138px; top: 212px; transform: translateX(-50%); font-size: 30px; }
  .brand-b { left: 295px; top: 158px; transform: translateX(-50%); font-size: 48px; }
  .brand-c { left: 100px; top: 42px; font-size: 28px; }
  .brand-d { left: 295px; top: 156px; transform: translateX(-50%); font-size: 48px; }

  .holder { position: absolute; right: 43px; text-align: right; font-size: 27px; line-height: 1; }
  .holder-a { top: 47px; }
  .holder-c { top: 27px; }
  .holder .name { display: block; color: var(--teal); }
  .holder .role { display: block; color: var(--gold); font-style: italic; margin-top: 3px; }

  .contacts { position: absolute; list-style: none; }
  .contacts-a { left: 330px; top: 168px; }
  .contacts-c { left: 26px; top: 181px; }
  .contact { display: flex; align-items: center; height: 34px; margin-bottom: 7px; font-size: 17px; color: var(--teal); }
  .contact:nth-child(3) { margin-bottom: 13px; }
  .contact svg { width: 34px; height: 32px; margin-right: 12px; flex: none; }
</style>
</head>
<body>

<section class="card card--front card-a">
  <p class="brand brand--teal brand-a">Novarra clean</p>
  <div class="holder holder-a"><span class="name">YOUR NAME</span><span class="role">directur</span></div>
  <ul class="contacts contacts-a">
    <li class="contact"><svg viewBox="0 0 34 32"><path d="M2 10 Q17 0 32 10 L30 14 L24 12 L24 9 Q17 7 10 9 L10 12 L4 14 Z" fill="var(--teal)"/><path d="M8 16 L12 11 H22 L26 16 V28 H8 Z" fill="var(--teal)"/><g fill="var(--white)"><rect x="13" y="17" width="2" height="2"/><rect x="16" y="17" width="2" height="2"/><rect x="19" y="17" width="2" height="2"/><rect x="13" y="20" width="2" height="2"/><rect x="16" y="20" width="2" height="2"/><rect x="19" y="20" width="2" height="2"/></g></svg>phone</li>
    <li class="contact"><svg viewBox="0 0 34 32"><rect x="2" y="6" width="30" height="21" fill="var(--teal)"/><path d="M2 6 L17 18 L32 6 M2 27 L13 15 M32 27 L21 15" stroke="var(--white)" stroke-width="1.5" fill="none"/></svg>e-mail</li>
    <li class="contact"><svg viewBox="0 0 34 32"><rect x="3" y="4" width="26" height="26" fill="none" stroke="var(--teal)" stroke-width="3"/><path d="M8 16 L14 24 L31 1" stroke="var(--teal)" stroke-width="3" fill="none"/></svg>website</li>
    <li class="contact"><svg viewBox="0 0 34 32"><path d="M6 14 L18 3 L30 14 H27 V22 H9 V14 Z" fill="none" stroke="var(--teal)" stroke-width="2"/><rect x="15" y="12" width="6" height="6" fill="var(--teal)"/><path d="M2 20 H10 V26 H32 V31 H2 Z" fill="var(--teal)"/></svg>home/office</li>
  </ul>
</section>

<section class="card card--back card-b">
  <p class="brand brand--white brand-b">Novarra clean</p>
</section>

<section class="card card--front card-c">
  <svg class="corner" viewBox="0 0 590 360" preserveAspectRatio="none" aria-hidden="true">
    <polygon points="0,0 130,0 0,118" fill="var(--teal)"/>
    <polygon points="130,0 138,0 0,126 0,118" fill="var(--gold)"/>
    <polygon points="590,242 590,360 462,360" fill="var(--teal)"/>
    <polygon points="590,234 590,242 462,360 454,360" fill="var(--gold)"/>
  </svg>
  <p class="brand brand--teal brand-c">Novarra clean</p>
  <div class="holder holder-c"><span class="name">YOUR NAME</span><span class="role">directur</span></div>
  <ul class="contacts contacts-c">
    <li class="contact"><svg viewBox="0 0 34 32"><path d="M2 10 Q17 0 32 10 L30 14 L24 12 L24 9 Q17 7 10 9 L10 12 L4 14 Z" fill="var(--teal)"/><path d="M8 16 L12 11 H22 L26 16 V28 H8 Z" fill="var(--teal)"/><g fill="var(--white)"><rect x="13" y="17" width="2" height="2"/><rect x="16" y="17" width="2" height="2"/><rect x="19" y="17" width="2" height="2"/><rect x="13" y="20" width="2" height="2"/><rect x="16" y="20" width="2" height="2"/><rect x="19" y="20" width="2" height="2"/></g></svg>phone</li>
    <li class="contact"><svg viewBox="0 0 34 32"><rect x="2" y="6" width="30" height="21" fill="var(--teal)"/><path d="M2 6 L17 18 L32 6 M2 27 L13 15 M32 27 L21 15" stroke="var(--white)" stroke-width="1.5" fill="none"/></svg>e-mail</li>
    <li class="contact"><svg viewBox="0 0 34 32"><rect x="3" y="4" width="26" height="26" fill="none" stroke="var(--teal)" stroke-width="3"/><path d="M8 16 L14 24 L31 1" stroke="var(--teal)" stroke-width="3" fill="none"/></svg>website</li>
    <li class="contact"><svg viewBox="0 0 34 32"><path d="M6 14 L18 3 L30 14 H27 V22 H9 V14 Z" fill="none" stroke="var(--teal)" stroke-width="2"/><rect x="15" y="12" width="6" height="6" fill="var(--teal)"/><path d="M2 20 H10 V26 H32 V31 H2 Z" fill="var(--teal)"/></svg>home/office</li>
  </ul>
</section>

<section class="card card--back card-d">
  <p class="brand brand--white brand-d">Novarra clean</p>
</section>

</body>
</html>
```